Business Card Design

I need a business card for a new company based in Australia called "MedLinkora".

Its a cloud program for GPs that allows them to search for the specialist they require using a simple user friendly tool.

I would like the colours to match those in the program (the colours in the logo attached).

The final design should reflect the programs clarity, ease of use and professionalism.

Target Market(s)

GPs and other Health Professionals

Industry/Entity Type

Business

Contact Information for Business Card

MedLinkora; The Trusted Clinician Index; Marla Ostrove CEO; 0438215906; marla@medlinkora.example; www.medlinkora.example

Requirements
Must have
• Must have the logo attached; the web address and my name and phone number
Nice to have
• the slogan "The Trusted Clinician Index"

```html
<!DOCTYPE html>
<html lang="en">
<head>
<meta charset="UTF-8">
<title>MedLinkora Business Card</title>
<link rel="stylesheet" href="https://fonts.googleapis.com/css2?family=Open+Sans:wght@300;400;600&family=Times+New+Roman&family=Tinos:wght@400&display=swap">
<style>
  :root {
    --page-bg: #e9e6e1;
    --card-white: #ffffff;
    --teal: #2fb3c6;
    --teal-dark: #1b8fa3;
    --teal-light: #8fd8e3;
    --brand-blue: #2aa8d8;
    --stripe-grey: #6f7175;
    --ink: #2d2d2d;
    --photo-light: #e6f1f6;
    --photo-mid: #a9c3d3;
  }
  * { margin: 0; padding: 0; box-sizing: border-box; }
  html, body { width: 705px; height: 1200px; overflow: hidden; }
  body {
    background: var(--page-bg);
    font-family: "Open Sans", Arial, sans-serif;
    position: relative;
  }
  .card {
    position: absolute;
    left: 52px;
    width: 600px;
    height: 343px;
    background: var(--card-white);
    border-radius: 16px;
    overflow: hidden;
    box-shadow: 0 6px 18px rgba(0,0,0,0.18);
  }
  .card-front { top: 150px; }
  .card-back { top: 707px; }

  /* Front */
  .front-photo {
    position: absolute;
    left: 0; top: 0;
    width: 100%; height: 100%;
    background: linear-gradient(120deg, var(--photo-mid) 0%, var(--photo-light) 45%, var(--card-white) 70%);
  }
  .front-shape { position: absolute; inset: 0; }
  .front-brand {
    position: absolute;
    right: 34px; top: 170px;
    text-align: right;
  }
  .brand-name {
    font-weight: 300;
    font-size: 62px;
    letter-spacing: -1px;
    line-height: 1;
    color: var(--brand-blue);
  }
  .brand-tagline {
    font-size: 14px;
    color: var(--teal-dark);
    margin-top: 6px;
    letter-spacing: 0.5px;
  }

  /* Back */
  .back-shape { position: absolute; inset: 0; }
  .back-brand {
    position: absolute;
    left: 30px; top: 128px;
    color: var(--card-white);
  }
  .back-brand .brand-name {
    color: var(--card-white);
    font-size: 44px;
  }
  .back-brand .brand-tagline {
    color: var(--card-white);
    font-size: 11px;
    margin-top: 3px;
  }
  .person {
    position: absolute;
    left: 30px; top: 222px;
    color: var(--card-white);
    font-family: "Tinos", "Times New Roman", serif;
  }
  .person-name { font-size: 21px; }
  .person-title { font-size: 14px; margin-top: 2px; }
  .contact {
    position: absolute;
    right: 30px; top: 52px;
    text-align: right;
    font-family: "Tinos", "Times New Roman", serif;
    font-size: 17px;
    line-height: 1.5;
    color: var(--ink);
  }
</style>
</head>
<body>

<section class="card card-front">
  <div class="front-photo" role="img" aria-label="Photograph of two doctors reviewing information together"></div>
  <svg class="front-shape" viewBox="0 0 600 343" preserveAspectRatio="none" aria-hidden="true">
    <path d="M0 300 C180 270 400 300 600 250 L600 343 L0 343 Z" fill="var(--teal)" opacity="0.85"/>
    <path d="M0 310 C180 280 400 312 600 262" stroke="var(--card-white)" stroke-width="5" fill="none"/>
  </svg>
  <div class="front-brand">
    <div class="brand-name">MedLinkora</div>
    <div class="brand-tagline">The Trusted Clinician Index</div>
  </div>
</section>

<section class="card card-back">
  <svg class="back-shape" viewBox="0 0 600 343" preserveAspectRatio="none" aria-hidden="true">
    <defs>
      <linearGradient id="tealBand" x1="0" y1="0" x2="1" y2="1">
        <stop offset="0" stop-color="var(--teal-light)"/>
        <stop offset="0.45" stop-color="var(--teal)"/>
        <stop offset="1" stop-color="var(--teal-dark)"/>
      </linearGradient>
    </defs>
    <path d="M0 0 L300 0 C330 120 360 240 330 343 L0 343 Z" fill="url(#tealBand)"/>
    <path d="M310 0 C342 120 372 240 345 343" stroke="var(--stripe-grey)" stroke-width="10" fill="none"/>
    <path d="M0 330 C200 300 420 290 600 200" stroke="var(--stripe-grey)" stroke-width="8" fill="none"/>
    <path d="M0 343 C200 318 420 308 600 222 L600 343 Z" fill="var(--teal)"/>
  </svg>
  <div class="back-brand">
    <div class="brand-name">MedLinkora</div>
    <div class="brand-tagline">The Trusted Clinician Index</div>
  </div>
  <div class="person">
    <div class="person-name">Marla Ostrove</div>
    <div class="person-title">CEO</div>
  </div>
  <div class="contact">
    <div>0438215906</div>
    <div>marla@medlinkora.example</div>
    <div>www.medlinkora.example</div>
  </div>
</section>

</body>
</html>
```